Ashworth Web Design Project

I need the front page and an internal page designed for this client's website. The logo is attached. Obviously the colors have to go with and/or work with the logo colors. I also attached a very rough brochure layout to help you see the direction we're going in with print materials. The rough site map is also attached. I see a slider on the homepage, the art for which I may come back to you to create. This clinic is in a very high end Dallas neighborhood. The hook is that it's a primary care and urgent facility with convenient hours.

I don't know how much this impacts your design, but this will be a Wordpress site and I'm using a framework called Struxo (struxo-demo.example). If Struxo proves to be inflexible, I'll have to get a template that allows me to execute your design.

This site (http://oakbendcareclinic.example) has the type and quality of content I will eventually have on the Ashworth site.

I just revised the brief for this project. I added the site map and added details to the overview and the "Must Have" section. Thank you for revisiting the brief. 

Reason: Christmas was a bad time to end it.

Target Market(s)

Women 25-54 with children living at home, income over $150k/year

Industry/Entity Type

Clinic

Requirements
Must have
• Masthead incorporating the logo
Followed by the primary nav
Slider on the home page below that
Dual nav - 1 with the nav in the attached site map
2 secondary nav with areas of healthcare
There will three blocks under the nav
1. It's about time (with a small blurb less than 50 words.
2. It's about choices (with small blurb)
3. It's about you (with small blurb)
Three footer blocks
patient check in link on every page
"No appointment? No problem" icon on every page

```html
<!DOCTYPE html>
<html lang="en">
<head>
<meta charset="utf-8">
<title>Ashworth Medical</title>
<link href="https://fonts.googleapis.com/css2?family=Open+Sans:wght@400;600;700&family=Cinzel:wght@600&display=swap" rel="stylesheet">
<style>
:root{
  --page:#eef1f4;
  --ink:#555a60;
  --ink-dark:#333a40;
  --green:#3c9a1c;
  --green-light:#5cbf2a;
  --green-dark:#2a7a10;
  --blue:#2d66b5;
  --blue-light:#4a88d4;
  --blue-dark:#1d4f95;
  --title-blue:#2a4d8f;
  --title-green:#56a82a;
  --bar:#25292d;
  --footer:#2c3136;
  --footer-line:#3c4248;
  --footer-text:#b8bec4;
  --white:#ffffff;
  --panel:#f3f4f6;
  --rule:#d8dce0;
}
*{box-sizing:border-box;margin:0;padding:0}
html,body{width:1090px;height:1200px;overflow:hidden}
body{position:relative;background:var(--page);font-family:Arial,Helvetica,sans-serif;color:var(--ink)}
.abs{position:absolute}
a{color:inherit;text-decoration:none}

.top-bar{left:0;top:0;width:1090px;height:22px;background:var(--bar)}
.top-links{right:142px;top:4px;display:flex;gap:22px;font:700 11px Arial,Helvetica,sans-serif;color:var(--white)}

.brand{left:138px;top:34px;display:flex;align-items:center;gap:10px}
.brand-mark{width:46px;height:46px;border-radius:50%;background:var(--blue)}
.brand-name{font:700 32px 'Open Sans',sans-serif;color:var(--green);line-height:1;letter-spacing:-0.5px}
.brand-tag{left:196px;top:76px;font:700 10px Arial,Helvetica,sans-serif;color:var(--ink-dark);white-space:nowrap}
.brand-tag::before,.brand-tag::after{content:"";display:inline-block;width:22px;height:1px;background:var(--ink-dark);vertical-align:middle;margin:0 5px}

.cta{top:42px;height:46px;border-radius:3px;display:flex;align-items:center;color:var(--white);font:700 14px 'Open Sans',sans-serif;gap:9px;padding-left:10px;white-space:nowrap}
.cta-walkin{left:605px;width:170px;background:linear-gradient(var(--green-light),var(--green-dark));line-height:1.15;font-size:13.5px}
.cta-check{left:782px;width:171px;background:linear-gradient(var(--blue-light),var(--blue-dark));font-size:17px;font-weight:600}

.main-nav{left:137px;top:108px;width:816px;height:42px;background:linear-gradient(#ffffff,#eceef0);border-radius:2px;box-shadow:0 3px 4px rgba(0,0,0,.18);display:flex}
.main-nav a{display:flex;align-items:center;justify-content:center;font:11px Arial,Helvetica,sans-serif;color:var(--ink-dark);border-right:1px solid var(--rule);height:100%}
.main-nav a.active{background:linear-gradient(var(--green-light),var(--green-dark));color:var(--white)}

.areas{left:137px;top:167px;width:186px;height:254px;background:linear-gradient(var(--blue-light),var(--blue-dark));border-radius:3px}
.areas-head{height:34px;display:flex;align-items:center;gap:10px;padding-left:10px;background:var(--blue-dark);border-radius:3px 3px 0 0;color:var(--white);font:600 14px 'Open Sans',sans-serif}
.areas ul{list-style:none;padding:0 8px}
.areas li{height:30px;display:flex;align-items:center;gap:6px;border-bottom:1px solid rgba(255,255,255,.22);color:var(--white);font:12px Arial,Helvetica,sans-serif}
.areas li:last-child{border-bottom:none}

.about-box{left:137px;width:186px;background:var(--panel);border-radius:3px;overflow:hidden}
.about-head{height:34px;display:flex;align-items:center;gap:8px;padding-left:8px;background:linear-gradient(var(--green-light),var(--green-dark));border-radius:3px 3px 0 0;color:var(--white);font:700 14px 'Open Sans',sans-serif}
.about-text{padding:8px 6px 0 8px;font:10.2px/15px Arial,Helvetica,sans-serif;white-space:nowrap}
.about-text b{color:var(--ink-dark)}

.content{left:337px;top:167px;width:616px;height:807px;background:var(--white)}
.slider{left:337px;top:167px;width:616px;height:273px;background:linear-gradient(100deg,#e9e2da 0%,#f4f2ee 45%,#e5e9ec 70%,#d9c9b8 100%);border:1px solid #d0d0d0}
.slide-title{left:580px;top:206px;font:600 28px 'Cinzel',serif;color:var(--title-blue);letter-spacing:1px}
.slide-sub{left:581px;top:240px;font:600 17px 'Cinzel',serif;color:var(--title-green);letter-spacing:1px}
.dots{left:625px;top:450px;display:flex;gap:4px}
.dots span{width:11px;height:11px;border-radius:50%;border:1px solid #b5bcc4;background:#f4f4f4}
.dots span.on{background:var(--blue-light);border-color:var(--blue-light)}

.welcome{left:357px;top:478px;display:flex;align-items:center;gap:10px;font:600 20px 'Open Sans',sans-serif;color:var(--title-green)}
.welcome em{font-style:normal;color:var(--title-blue)}
.dot-icon{border-radius:50%;background:var(--blue);flex:none}
.welcome-rule{left:357px;top:520px;width:577px;border-top:1px dotted #bbb}
.welcome-text{left:356px;top:530px;width:580px;font:10.5px/16px Arial,Helvetica,sans-serif;letter-spacing:.35px}
.read-more{display:flex;align-items:center;gap:5px;font:700 11px Arial,Helvetica,sans-serif;color:var(--green-dark);white-space:nowrap}
.plus{width:13px;height:13px;border-radius:50%;background:var(--green);color:var(--white);font:700 12px/13px Arial,sans-serif;text-align:center}

.services{left:354px;top:664px;width:583px;height:284px;border:1px solid var(--rule);border-radius:5px;background:linear-gradient(#f6f7f8,#ffffff 40%);box-shadow:0 2px 3px rgba(0,0,0,.1)}
.service{position:absolute;top:14px;width:178px;height:264px}
.service h3{display:flex;align-items:center;gap:6px;font:600 12.5px 'Open Sans',sans-serif;color:var(--title-green);margin-left:2px;white-space:nowrap;height:20px}
.service h3 em{font-style:normal;color:var(--title-blue)}
.service .thumb{margin-top:12px;width:178px;height:108px;border:1px solid #ccc}
.service p{margin-top:12px;padding:0 4px;font:10.3px/15px Arial,Helvetica,sans-serif}
.service p b{color:var(--ink-dark)}
.service .read-more{position:absolute;top:249px;left:0;color:#7a8088;font-weight:400}

.footer{left:0;top:974px;width:1090px;height:188px;background:var(--footer);border-top:3px solid var(--blue)}
.foot-title{font:15px 'Open Sans',sans-serif;color:var(--white);padding-bottom:8px;border-bottom:2px solid #15181b;width:230px}
.quick{left:138px;top:992px}
.quick-grid{display:grid;grid-template-columns:110px 110px;column-gap:12px;margin-top:6px}
.quick-grid a{height:26px;display:flex;align-items:center;gap:10px;padding-left:9px;font:10.5px Arial,Helvetica,sans-serif;color:var(--footer-text);border-bottom:1px solid var(--footer-line)}
.quick-grid a::before{content:"";border-left:6px solid var(--green-light);border-top:4px solid transparent;border-bottom:4px solid transparent}
.quick-grid a.current{background:#1b1e21;color:var(--white)}
.newsletter{left:461px;top:992px}
.newsletter .foot-title{width:184px}
.newsletter p{margin-top:16px;width:200px;font:10.5px/16px Arial,Helvetica,sans-serif;color:var(--footer-text)}
.email-field{margin-top:12px;width:173px;height:30px;background:var(--white);border-radius:3px;display:flex;align-items:center;gap:8px;padding-left:8px;font:10.5px Arial,sans-serif;color:#b8b8b8}
.subscribe{margin-top:18px;width:84px;height:24px;border-radius:2px;background:linear-gradient(var(--green-light),var(--green-dark));color:var(--white);font:700 11px Arial,sans-serif;display:flex;align-items:center;justify-content:center}
.contact{left:738px;top:992px}
.contact .foot-title{width:186px}
.contact-row{display:flex;align-items:center;gap:12px;font:10.5px/14px Arial,Helvetica,sans-serif;color:var(--white);margin-top:14px}
.socials{display:flex;gap:8px;margin:12px 0 0 32px}
.socials span{width:19px;height:19px;border-radius:3px}
.legal{left:0;top:1162px;width:1090px;height:38px;display:flex;align-items:center;justify-content:center;gap:10px;font:10.5px Arial,Helvetica,sans-serif;color:var(--ink-dark)}
</style>
</head>
<body>

<div class="abs top-bar"></div>
<nav class="abs top-links"><a href="#">Register</a><a href="#">Log In</a><a href="#">Blog</a></nav>

<div class="abs brand"><span class="brand-mark"></span><span class="brand-name">AshworthMedical</span></div>
<div class="abs brand-tag">Immediate Family and Personal Care</div>

<a class="abs cta cta-walkin" href="#">
  <svg width="26" height="24" viewBox="0 0 26 24"><path d="M13 1 L25 23 H1 Z" fill="#fff"/><rect x="11.8" y="8" width="2.4" height="8" fill="#3c9a1c"/><rect x="11.8" y="18" width="2.4" height="2.4" fill="#3c9a1c"/></svg>
  <span>No appointment?<br>No problem</span>
</a>
<a class="abs cta cta-check" href="#">
  <svg width="24" height="24" viewBox="0 0 24 24"><rect x="1" y="1" width="22" height="22" rx="3" fill="#fff"/><rect x="10" y="5" width="4" height="14" fill="#2d66b5"/><rect x="5" y="10" width="14" height="4" fill="#2d66b5"/></svg>
  <span>Patient Check</span>
</a>

<nav class="abs main-nav">
  <a class="active" href="#" style="width:85px">HOME</a>
  <a href="#" style="width:104px">ABOUT US</a>
  <a href="#" style="width:98px">SERVICES</a>
  <a href="#" style="width:82px">STAFF</a>
  <a href="#" style="width:111px">INSURANCE</a>
  <a href="#" style="width:127px">SCHOLARSHIPS</a>
  <a href="#" style="width:94px">VIDEOS</a>
  <a href="#" style="width:115px;border-right:none">CONTACT US</a>
</nav>

<aside class="abs areas">
  <div class="areas-head">
    <svg width="22" height="22" viewBox="0 0 22 22"><rect x="8" y="1" width="6" height="20" fill="#fff"/><rect x="1" y="8" width="20" height="6" fill="#fff"/></svg>
    Areas Of Healthcare
  </div>
  <ul>
    <li>› IMMEDIATE CARE</li>
    <li>› ALLERGIES</li>
    <li>› PRIMARY CARE</li>
    <li>› WOMEN'S HEALTH</li>
    <li>› MEDICAL SPA TREATMENTS</li>
    <li>› MEN'S HEALTH</li>
    <li>› WEIGHT LOSS</li>
  </ul>
</aside>

<section class="abs about-box" style="top:433px;height:199px">
  <div class="about-head">
    <svg width="24" height="24" viewBox="0 0 24 24" fill="none" stroke="#fff" stroke-width="2"><circle cx="12" cy="13" r="9"/><path d="M12 8v5l3 2M3 5l4-3M21 5l-4-3"/></svg>
    It's About Time
  </div>
  <p class="about-text"><b>Lorem ipsum dolor sit amet</b><br>consectetuer adipiscing elit, sed iam<br>nonummy nibh euismod tincidunt ut<br>laoreet dolore magna aliquam erat<br>volutpat.Ut wisi enim ad minim niam,<br>quis nostrud exelLorem ipsum olor<br>sit ametconsectetuer adipiscing elit,<br>sed iam nonummy nibh euismod nnt<br>ut laoreet dolore magna aliquam Aat<br>volutpat.Ut wisi enim ad minim</p>
</section>

<section class="abs about-box" style="top:650px;height:136px">
  <div class="about-head">
    <svg width="24" height="24" viewBox="0 0 24 24"><circle cx="12" cy="12" r="10" fill="none" stroke="#fff" stroke-width="2"/><text x="12" y="17" text-anchor="middle" font-family="Arial" font-weight="700" font-size="14" fill="#fff">?</text></svg>
    It's About Choices
  </div>
  <p class="about-text"><b>Lorem ipsum dolor sit amet</b><br>consectetuer adipiscing elit, sed iam<br>nonummy nibh euismod tincidunt ut<br>laoreet dolore magna aliquam erat<br>volutpat.Ut wisi enim ad minim<br>niam, quis nostrud exve.</p>
</section>

<section class="abs about-box" style="top:805px;height:144px">
  <div class="about-head">
    <svg width="30" height="20" viewBox="0 0 30 20" fill="none" stroke="#fff" stroke-width="2"><rect x="1" y="5" width="6" height="12"/><path d="M7 7h10l10-1M7 15h12M17 7v8"/></svg>
    It's About You
  </div>
  <p class="about-text"><b>Lorem ipsum dolor sit amet</b><br>consectetuer adipiscing elit, sed iam<br>nonummy nibh euismod tincidunt ut<br>laoreet dolore magna aliquam erat<br>volutpat.Ut wisi enim ad minim<br>niam, quis nostrud exve.</p>
</section>

<div class="abs content"></div>
<div class="abs slider" role="img" aria-label="Slider photo: a nurse holding the hand of a smiling patient resting in bed at home"></div>
<div class="abs slide-title">Exceptional Care</div>
<div class="abs slide-sub">In the comfort of your home</div>
<div class="abs dots"><span></span><span class="on"></span><span></span></div>

<h1 class="abs welcome"><span class="dot-icon" style="width:30px;height:30px"></span>Welcome To <em>Ashworth Medical</em></h1>
<div class="abs welcome-rule"></div>
<p class="abs welcome-text">Lorem ipsum dolor sit amet, consectetuer adipiscing elit, sed diam nonummy nibh euismod tincidunt ut laoreet dolore magna aliquam erat volutpat. Ut wisi enim ad minim veniam, quis nostrud exerci tation ullamcorper suscipit lobortis nisl ut aliquip ex ea commodo consequat. Duis autem vel eum iriure dolor in hendrerit in vulputate velit esse molestie consequat, vel illum dolore eu feugiat nulla facilisis at vero eros et accumsan et iusto odio dignissim qui blandit praesent luptatum zzril delenit augue duis dolore te feugait nulla facilisi.</p>
<a class="abs read-more" href="#" style="left:866px;top:615px"><span class="plus">+</span>Read More</a>

<section class="abs services">
  <div class="service" style="left:11px">
    <h3><span class="dot-icon" style="width:17px;height:17px"></span>Primary <em>Care</em></h3>
    <div class="thumb" role="img" aria-label="Photo: a child having her temperature taken" style="background:linear-gradient(120deg,#e8c9b4,#d98fa8 60%,#c7a58e)"></div>
    <p><b>Lorem ipsum dolor sit amet</b><br>consectetuer adipiscing elit, sed iam nonummy nibh euismod tincidunt ut laoreet dolore magna aliquam erat volutpat.Ut wisi enim.</p>
    <a class="read-more" href="#"><span class="plus">+</span>Read More</a>
  </div>
  <div class="service" style="left:202px">
    <h3><span class="dot-icon" style="width:17px;height:17px"></span>Immediate <em>Care</em></h3>
    <div class="thumb" role="img" aria-label="Photo: paramedics attending a patient on a stretcher" style="background:linear-gradient(120deg,#3a3f4a,#c9a52a 45%,#7a2f2f 80%,#2f3440)"></div>
    <p><b>Lorem ipsum dolor sit amet</b><br>consectetuer adipiscing elit, sed iam nonummy nibh euismod tincidunt ut laoreet dolore magna aliquam erat volutpat.Ut wisi enim .</p>
    <a class="read-more" href="#"><span class="plus">+</span>Read More</a>
  </div>
  <div class="service" style="left:394px">
    <h3><span class="dot-icon" style="width:17px;height:17px"></span>Medical <em>Spa Treatments</em></h3>
    <div class="thumb" role="img" aria-label="Photo: a spa treatment room with a client on a treatment chair" style="background:linear-gradient(120deg,#e9e6e2,#c9c2bd 55%,#6a5d5a)"></div>
    <p><b>Lorem ipsum dolor sit amet</b><br>consectetuer adipiscing elit, sed iam nonummy nibh euismod tincidunt ut laoreet dolore magna aliquam erat volutpat.Ut wisi enim.</p>
    <a class="read-more" href="#"><span class="plus">+</span>Read More</a>
  </div>
</section>

<footer class="abs footer"></footer>

<div class="abs quick">
  <div class="foot-title">Quick Links</div>
  <div class="quick-grid">
    <a href="#">Home</a><a href="#">Scholarships</a>
    <a class="current" href="#">About Us</a><a href="#">Videos</a>
    <a href="#">Services</a><a href="#">Contact Us</a>
    <a href="#">Staff</a><a href="#">Site Map</a>
    <a href="#">Insurance</a><a href="#">Terms of Service</a>
  </div>
</div>

<div class="abs newsletter">
  <div class="foot-title">Newsletter</div>
  <p>Get updates about promotions and new products by entering e-mail</p>
  <div class="email-field">
    <svg width="20" height="14" viewBox="0 0 20 14" fill="none" stroke="#c4c4c4" stroke-width="1.4"><rect x="1" y="1" width="18" height="12"/><path d="M1 1l9 7 9-7"/></svg>
    your e-mail address
  </div>
  <div class="subscribe">Subscribe</div>
</div>

<div class="abs contact">
  <div class="foot-title">Contact Details</div>
  <div class="contact-row">
    <svg width="20" height="18" viewBox="0 0 20 18"><path d="M10 1 L19 9 H16 V17 H12 V12 H8 V17 H4 V9 H1 Z" fill="#fff"/></svg>
    <span>Donec et nibh mauris. nibh<br>varius at euismod risus eleifend.</span>
  </div>
  <div class="contact-row">
    <svg width="20" height="18" viewBox="0 0 20 18"><path d="M6 2c-2 1-3 3-2 6 2 4 5 7 8 8 2 1 4 0 5-2l-3-3-2 2c-2-1-4-3-5-5l2-2z" fill="#fff"/></svg>
    <span>555.014.2270</span>
  </div>
  <div class="contact-row">
    <svg width="20" height="18" viewBox="0 0 20 18"><text x="10" y="15" text-anchor="middle" font-family="Arial" font-weight="700" font-size="18" fill="#fff">@</text></svg>
    <span>info@ashworthmedical.example</span>
  </div>
  <div class="socials">
    <span style="background:#4fb3e0"></span><span style="background:#3b5a99"></span><span style="background:#c9302c"></span>
  </div>
</div>

<div class="abs legal"><span>©2012. Ashworth Medical. All right reserved.</span><span>|</span><a href="#">Privacy Policy</a></div>

</body>
</html>
```